Business Card Design Project

Business Card
We are rebranding with a new logo
Industry/Entity Type
Business
Contact Information for Business Card
Dennis Marlow +61 427581962 dennis@qovo.com.au P.O. Box 872 Kelvindale QLD 4309
Requirements
Must have
- Logo

```html
<!DOCTYPE html>
<html lang="en">
<head>
<meta charset="utf-8">
<title>Qovo International – Business Cards</title>
<link rel="stylesheet" href="https://fonts.googleapis.com/css2?family=Montserrat:wght@500;600;700&display=swap">
<style>
  :root {
    --backdrop: #ececec;
    --brand-blue: #0f7aa2;
    --brand-blue-light: #2a98c0;
    --brand-blue-dark: #0a6386;
    --swoosh-grey: #6b6b6b;
    --paper: #ffffff;
    --ink-white: #ffffff;
  }
  * { box-sizing: border-box; margin: 0; padding: 0; }
  html, body { width: 1200px; height: 1200px; overflow: hidden; }
  body {
    background: var(--backdrop);
    font-family: "Montserrat", Arial, sans-serif;
    position: relative;
  }
  .card {
    position: absolute;
    left: 300px;
    width: 600px;
    height: 360px;
    overflow: hidden;
  }
  /* Front */
  .card-front {
    top: 190px;
    background: radial-gradient(ellipse at 50% 35%, var(--brand-blue-light) 0%, var(--brand-blue) 55%, var(--brand-blue-dark) 100%);
    color: var(--ink-white);
    text-align: center;
  }
  .card-front .wordmark {
    position: absolute;
    top: 92px;
    left: 0; right: 0;
    font-weight: 600;
    color: var(--ink-white);
    line-height: 1;
  }
  .card-front .wordmark-name { display: block; font-size: 86px; letter-spacing: 1px; }
  .card-front .wordmark-sub { display: block; font-size: 22px; letter-spacing: 3px; margin-top: 10px; }
  .card-front .web {
    position: absolute;
    bottom: 30px; left: 0; right: 0;
    font-size: 12px;
    letter-spacing: 4px;
    font-weight: 500;
  }
  /* Back */
  .card-back {
    top: 650px;
    background: var(--paper);
  }
  .card-back .wordmark {
    position: absolute;
    top: 30px; left: 28px;
    font-weight: 600;
    color: var(--brand-blue);
    line-height: 1;
  }
  .card-back .wordmark-name { display: block; font-size: 56px; }
  .card-back .wordmark-sub { display: block; font-size: 15px; letter-spacing: 2px; margin-top: 6px; }
  .contact {
    position: absolute;
    right: 28px; top: 158px;
    text-align: right;
    color: var(--brand-blue);
  }
  .contact .person-name { font-size: 31px; font-weight: 600; margin-bottom: 22px; }
  .contact .line {
    font-size: 15px; font-weight: 600;
    display: flex; justify-content: flex-end; align-items: center; gap: 10px;
    margin-bottom: 6px;
  }
  .contact svg { width: 14px; height: 14px; }
  .wave { position: absolute; left: 0; bottom: 0; width: 600px; height: 150px; }
  .address {
    position: absolute;
    left: 0; right: 0; bottom: 28px;
    color: var(--ink-white);
    font-size: 15px; font-weight: 600;
    display: flex; justify-content: center; align-items: center; gap: 10px;
  }
  .address svg { width: 14px; height: 14px; }
</style>
</head>
<body>
  <section class="card card-front">
    <div class="wordmark">
      <span class="wordmark-name">Qovo</span>
      <span class="wordmark-sub">INTERNATIONAL</span>
    </div>
    <div class="web">www.qovo.com.au</div>
  </section>

  <section class="card card-back">
    <div class="wordmark">
      <span class="wordmark-name">Qovo</span>
      <span class="wordmark-sub">INTERNATIONAL</span>
    </div>
    <svg class="wave" viewBox="0 0 600 150" preserveAspectRatio="none">
      <defs>
        <linearGradient id="bandFill" x1="0" y1="0" x2="0" y2="1">
          <stop offset="0" stop-color="#2a98c0"/>
          <stop offset="1" stop-color="#0a6386"/>
        </linearGradient>
      </defs>
      <path d="M0,18 C150,70 420,70 600,42" fill="none" stroke="#6b6b6b" stroke-width="5"/>
      <path d="M0,32 C160,88 420,86 600,55 L600,150 L0,150 Z" fill="url(#bandFill)"/>
    </svg>
    <div class="contact">
      <div class="person-name">Dennis Marlow</div>
      <div class="line">+61 427581962
        <svg viewBox="0 0 14 14"><circle cx="7" cy="7" r="6" fill="none" stroke="currentColor" stroke-width="1.2"/><path d="M5,4 L6,4 L6.5,6 L5.8,6.6 C6.3,7.6 6.9,8.2 7.6,8.6 L8.2,7.9 L10,8.5 L10,9.6 C7,10 4.2,7 5,4 Z" fill="currentColor"/></svg>
      </div>
      <div class="line">dennis@qovo.com.au
        <svg viewBox="0 0 14 14"><circle cx="7" cy="7" r="6" fill="none" stroke="currentColor" stroke-width="1.2"/><rect x="3.8" y="4.8" width="6.4" height="4.4" fill="none" stroke="currentColor" stroke-width="1"/><path d="M3.8,4.8 L7,7.4 L10.2,4.8" fill="none" stroke="currentColor" stroke-width="1"/></svg>
      </div>
    </div>
    <div class="address">
      <svg viewBox="0 0 14 14"><circle cx="7" cy="7" r="6" fill="none" stroke="currentColor" stroke-width="1.2"/><path d="M7,3.5 C5.4,3.5 4.5,4.6 4.5,5.8 C4.5,7.6 7,10.5 7,10.5 C7,10.5 9.5,7.6 9.5,5.8 C9.5,4.6 8.6,3.5 7,3.5 Z" fill="currentColor"/></svg>
      P.O. Box 872 Kelvindale QLD 4309
    </div>
  </section>
</body>
</html>
```